Full redesign of dairy products including Yogurts and milk products

We have been selling milk and yogurts over the past 15 years, we are now expanding into a wider range of dairy products to include flavoured milk and a variety of soft cheeses such as cottage cheese etc. It is now the perfect time to redesign our existing product range to give a fresh and new look to our products. Have a look at our website https://rtvale.co.uk/ for further details. We are rebranding as NUVELKA, I have attached a identify pack to give you a feel of the the design, this is a fresh and bright design that will reflect the fresh and tasteful products we produce. The current milk label cut out is unique to us and I would like to continue using this shape which I have attached, the other labels should be done using regular rectangular rounded edge labels. The following designs are required;
1 x Universal lid (71.5mm) design for all below 120ml Yogurts
-11 x 120 ml Yogurt pot designs
Strawberry
Strawberry Banana
Peach & Apricot
Cherry
Toffee
Vanilla
Natural
Orange
Forest Fruits
Pineapple
Mango
1 x Universal lid (95.5mm)for below yogurts (can be identical to the 120ml Lid)
-4 x 450ml Yogurt Pots
Strawberry
Natural
Toffee
Mango
-1 x Universal (95.5mm) LID for 150ml Greek Yogurt
-4 x Designs for 150ml Greek yogurt POT
Strawberry
Natural
Vanilla
Mango

3 x Flavoured milk labels 2 sizes 250ml & 1lt
Biscotti
Chocolate
Strawberry

Cottage Cheese Lid & Pot 250g

1 x Quark universal Lid (95.5mm)
4 x Quark 250g pots
Natural
Strawberry
Peach & Apricot
Mango

```html
<!DOCTYPE html>
<html lang="en">
<head>
<meta charset="utf-8">
<title>NUVELKA Yogurt – Mango, Forest Fruits, Pineapple</title>
<link rel="stylesheet" href="https://fonts.googleapis.com/css2?family=Marcellus&display=swap">
<style>
  :root {
    --bg: #ececec;
    --pot: #f7f7f7;
    --pot-edge: #e2e2e2;
    --ink: #141414;
    --brand-green: #5cbd4b;
    --mango: #de5a4b;
    --forest: #c23f87;
    --pineapple: #e9c01c;
    --white: #ffffff;
  }
  * { box-sizing: border-box; margin: 0; padding: 0; }
  html, body { width: 1200px; height: 967px; overflow: hidden; }
  body {
    background: var(--bg);
    font-family: "Marcellus", serif;
    color: var(--ink);
  }
  .range {
    position: relative;
    width: 1200px;
    height: 967px;
    display: flex;
    justify-content: center;
    gap: 70px;
    padding-top: 90px;
  }
  .flavour {
    width: 290px;
    display: flex;
    flex-direction: column;
    align-items: center;
    gap: 40px;
  }
  .flavour--mango { --accent: var(--mango); --fruit-a: #f2b437; --fruit-b: #d9463a; }
  .flavour--forest { --accent: var(--forest); --fruit-a: #d8374f; --fruit-b: #2a2433; }
  .flavour--pineapple { --accent: var(--pineapple); --fruit-a: #f6d339; --fruit-b: #7c8a2e; }

  /* Lid */
  .lid { width: 250px; height: 250px; display: block; }
  .lid__ring { fill: var(--accent); }
  .lid__face { fill: var(--white); }
  .lid__rim-text { font-family: "Marcellus", serif; font-size: 8.6px; letter-spacing: 0.6px; fill: var(--ink); }
  .lid__brand { font-family: "Marcellus", serif; font-size: 22px; fill: var(--brand-green); letter-spacing: 1px; }
  .lid__title { font-family: "Marcellus", serif; font-size: 21px; fill: var(--ink); letter-spacing: 3px; }

  /* Pot wrap */
  .pot {
    width: 270px;
    height: 400px;
    background: linear-gradient(90deg, var(--pot-edge) 0%, var(--pot) 18%, var(--white) 50%, var(--pot) 82%, var(--pot-edge) 100%);
    border-radius: 14px 14px 22px 22px;
    display: flex;
    flex-direction: column;
    align-items: center;
    overflow: hidden;
    clip-path: polygon(0 0, 100% 0, 95% 100%, 5% 100%);
  }
  .pot__brand {
    margin-top: 42px;
    font-size: 40px;
    color: var(--brand-green);
    letter-spacing: 2px;
  }
  .pot__title {
    margin-top: 26px;
    font-size: 44px;
    letter-spacing: 3px;
    line-height: 1;
  }
  .pot__fruit {
    margin-top: 28px;
    width: 190px;
    height: 110px;
    border-radius: 50%;
    background: radial-gradient(ellipse at 40% 45%, var(--fruit-a) 0%, var(--fruit-b) 100%);
  }
  .pot__band {
    margin-top: auto;
    margin-bottom: 26px;
    width: 100%;
    height: 48px;
    background: var(--accent);
    display: flex;
    align-items: center;
    justify-content: center;
    color: var(--white);
    font-size: 16px;
    letter-spacing: 1.5px;
  }
  .flavour--pineapple .pot__band { color: var(--ink); }
</style>
</head>
<body>
<main class="range">

  <section class="flavour flavour--mango">
    <svg class="lid" viewBox="0 0 250 250" aria-label="Mango yogurt lid">
      <defs><path id="rim-mango" d="M125,125 m-107,0 a107,107 0 1,1 214,0 a107,107 0 1,1 -214,0"/></defs>
      <circle class="lid__ring" cx="125" cy="125" r="124"/>
      <circle class="lid__face" cx="125" cy="125" r="114"/>
      <text class="lid__rim-text"><textPath href="#rim-mango">Keep refrigerated below five degrees and enjoy within three days of opening · Made with fresh whole milk and live cultures ·</textPath></text>
      <text class="lid__brand" x="125" y="72" text-anchor="middle">NUVELKA</text>
      <text class="lid__title" x="125" y="110" text-anchor="middle">YOGURT</text>
      <ellipse cx="125" cy="150" rx="60" ry="22" fill="url(#g-mango)" role="img" aria-label="Mango fruit photograph"/>
      <defs><radialGradient id="g-mango"><stop offset="0" stop-color="#f2b437"/><stop offset="1" stop-color="#d9463a"/></radialGradient></defs>
    </svg>
    <div class="pot">
      <div class="pot__brand">NUVELKA</div>
      <h2 class="pot__title">YOGURT</h2>
      <div class="pot__fruit" role="img" aria-label="Whole and sliced mango photograph"></div>
      <div class="pot__band">MANGO</div>
    </div>
  </section>

  <section class="flavour flavour--forest">
    <svg class="lid" viewBox="0 0 250 250" aria-label="Forest fruits yogurt lid">
      <defs><path id="rim-forest" d="M125,125 m-107,0 a107,107 0 1,1 214,0 a107,107 0 1,1 -214,0"/></defs>
      <circle class="lid__ring" cx="125" cy="125" r="124"/>
      <circle class="lid__face" cx="125" cy="125" r="114"/>
      <text class="lid__rim-text"><textPath href="#rim-forest">Keep refrigerated below five degrees and enjoy within three days of opening · Made with fresh whole milk and live cultures ·</textPath></text>
      <text class="lid__brand" x="125" y="72" text-anchor="middle">NUVELKA</text>
      <text class="lid__title" x="125" y="110" text-anchor="middle">YOGURT</text>
      <ellipse cx="125" cy="150" rx="60" ry="22" fill="url(#g-forest)" role="img" aria-label="Mixed berries photograph"/>
      <defs><radialGradient id="g-forest"><stop offset="0" stop-color="#d8374f"/><stop offset="1" stop-color="#2a2433"/></radialGradient></defs>
    </svg>
    <div class="pot">
      <div class="pot__brand">NUVELKA</div>
      <h2 class="pot__title">YOGURT</h2>
      <div class="pot__fruit" role="img" aria-label="Raspberries, blueberries and blackberries photograph"></div>
      <div class="pot__band">FOREST FRUITS</div>
    </div>
  </section>

  <section class="flavour flavour--pineapple">
    <svg class="lid" viewBox="0 0 250 250" aria-label="Pineapple yogurt lid">
      <defs><path id="rim-pine" d="M125,125 m-107,0 a107,107 0 1,1 214,0 a107,107 0 1,1 -214,0"/></defs>
      <circle class="lid__ring" cx="125" cy="125" r="124"/>
      <circle class="lid__face" cx="125" cy="125" r="114"/>
      <text class="lid__rim-text"><textPath href="#rim-pine">Keep refrigerated below five degrees and enjoy within three days of opening · Made with fresh whole milk and live cultures ·</textPath></text>
      <text class="lid__brand" x="125" y="72" text-anchor="middle">NUVELKA</text>
      <text class="lid__title" x="125" y="110" text-anchor="middle">YOGURT</text>
      <ellipse cx="125" cy="150" rx="60" ry="22" fill="url(#g-pine)" role="img" aria-label="Pineapple photograph"/>
      <defs><radialGradient id="g-pine"><stop offset="0" stop-color="#f6d339"/><stop offset="1" stop-color="#7c8a2e"/></radialGradient></defs>
    </svg>
    <div class="pot">
      <div class="pot__brand">NUVELKA</div>
      <h2 class="pot__title">YOGURT</h2>
      <div class="pot__fruit" role="img" aria-label="Whole and sliced pineapple photograph"></div>
      <div class="pot__band">PINEAPPLE</div>
    </div>
  </section>

</main>
</body>
</html>
```